Ashford Vale Crematory
Larkmoor, MN
Project: Ashford Vale Crematory
Ashford Vale Crematory -
Creative Brief
Simple
Paul Dorsey III
2873 Fennel St. Larkmoor, MN 58317
harlowbrenton@examplemail.net

```html
<!DOCTYPE html>
<html lang="en">
<head>
<meta charset="utf-8">
<title>Ashford Vale Crematory – Stationery</title>
<link rel="stylesheet" href="https://fonts.googleapis.com/css2?family=Cormorant+Garamond:wght@600&family=Open+Sans:wght@400;600&display=swap">
<style>
  :root {
    --navy: #3a3f6e;
    --paper: #ffffff;
    --backdrop: #8c8c8e;
    --ink-soft: #6b6e86;
    --watermark: #eef0f4;
  }
  * { margin: 0; padding: 0; box-sizing: border-box; }
  html, body { width: 1200px; height: 626px; overflow: hidden; }
  body {
    background: var(--backdrop);
    font-family: "Open Sans", sans-serif;
    position: relative;
  }
  .sheet { position: absolute; background: var(--paper); overflow: hidden; }
  .brand {
    font-family: "Cormorant Garamond", serif;
    font-weight: 600;
    color: var(--navy);
    text-align: center;
    line-height: 1.05;
    display: flex;
    flex-direction: column;
    align-items: center;
    gap: 3px;
    white-space: nowrap;
  }
  .brand-dot { border-radius: 50%; background: var(--navy); }
  .band { position: absolute; left: 0; right: 0; background: var(--navy); }
  .fine-print {
    position: absolute; left: 0; right: 0;
    text-align: center; color: var(--ink-soft);
    font-size: 4.6px; letter-spacing: 0.1px; white-space: nowrap;
  }

  /* Business card */
  .business-card { left: 34px; top: 307px; width: 165px; height: 101px; }
  .business-card .band { height: 4px; }
  .business-card .band.top { top: 0; }
  .business-card .band.bottom { bottom: 0; }
  .business-card .brand { position: absolute; left: 0; right: 0; top: 16px; font-size: 7px; }
  .business-card .brand-dot { width: 8px; height: 8px; }
  .card-holder {
    position: absolute; left: 0; right: 0; top: 56px;
    text-align: center; font-size: 5px; font-weight: 600; color: var(--navy);
  }
  .card-contact {
    position: absolute; left: 0; right: 0; top: 74px;
    text-align: center; font-size: 3.6px; color: var(--ink-soft); line-height: 1.5;
  }

  /* Letterhead */
  .letterhead { left: 233px; top: 29px; width: 427px; height: 564px; }
  .letterhead .band { height: 12px; }
  .letterhead .band.top { top: 0; }
  .letterhead .band.bottom { bottom: 0; }
  .letterhead .brand { position: absolute; left: 0; right: 0; top: 26px; font-size: 13px; }
  .letterhead .brand-dot { width: 16px; height: 16px; }
  .letterhead .watermark {
    position: absolute; left: 123px; top: 160px; width: 180px; height: 180px;
    border-radius: 50%; background: var(--watermark);
  }
  .letterhead .fine-print { bottom: 20px; }

  /* Envelope back */
  .envelope-back { left: 679px; top: 77px; width: 492px; height: 223px; }
  .envelope-back svg { position: absolute; inset: 0; }

  /* Envelope front */
  .envelope-front { left: 679px; top: 331px; width: 492px; height: 262px; }
  .envelope-front .band { height: 14px; }
  .envelope-front .band.top { top: 0; }
  .envelope-front .band.bottom { bottom: 0; }
  .envelope-front .brand { position: absolute; left: 0; right: 0; top: 48px; font-size: 12px; }
  .envelope-front .brand-dot { width: 15px; height: 15px; }
  .envelope-front .fine-print { bottom: 30px; font-size: 5px; }
</style>
</head>
<body>

  <section class="sheet business-card" aria-label="Business card">
    <div class="band top"></div>
    <div class="brand"><span class="brand-dot"></span><span>Ashford Vale Crematory</span></div>
    <p class="card-holder">Paul Dorsey III</p>
    <p class="card-contact">P: 555.014.2290 &nbsp; F: 555.014.2291<br>harlowbrenton@examplemail.net<br>2873 Fennel St. Larkmoor, MN 58317</p>
    <div class="band bottom"></div>
  </section>

  <section class="sheet letterhead" aria-label="Letterhead">
    <div class="band top"></div>
    <div class="brand"><span class="brand-dot"></span><span>Ashford Vale Crematory</span></div>
    <div class="watermark" role="img" aria-label="Faint brand emblem"></div>
    <p class="fine-print">P: 555.014.2290 &nbsp;|&nbsp; F: 555.014.2291 &nbsp;|&nbsp; harlowbrenton@examplemail.net &nbsp;|&nbsp; 2873 Fennel St. Larkmoor, MN 58317</p>
    <div class="band bottom"></div>
  </section>

  <section class="sheet envelope-back" aria-label="Envelope back">
    <svg width="492" height="223" viewBox="0 0 492 223" aria-hidden="true">
      <polygon points="0,0 492,0 492,48 246,152 0,48" fill="var(--navy)"/>
      <polyline points="0,223 246,120 492,223" fill="none" stroke="#e3e4ea" stroke-width="1"/>
    </svg>
  </section>

  <section class="sheet envelope-front" aria-label="Envelope front">
    <div class="band top"></div>
    <div class="brand"><span class="brand-dot"></span><span>Ashford Vale Crematory</span></div>
    <p class="fine-print">P: 555.014.2290 &nbsp;|&nbsp; F: 555.014.2291 &nbsp;|&nbsp; harlowbrenton@examplemail.net &nbsp;|&nbsp; 2873 Fennel St. Larkmoor, MN 58317</p>
    <div class="band bottom"></div>
  </section>

</body>
</html>
```